Grins of Maplecrest - Dental, needs a redesign

Purpose:
Redesign website: http://www.grinsofmaplecrest.example/

Sections are important, but for content, we can use existing website or have some placeholder text to fill in later.

Some of the required sections:
About us, contact us, services, our offices, our staff, patient education, patient forms (link to Molvaro can be used here), link to friendwall, testimonials

Editability:
We would like to be able to update and edit the content in the future, for small changes

Pictures:
Here is a link to the staff pictures we’d like to use on the website:
https://www.filecrate.example/sh/503k7pq2vv884x9/BBDPyrTe_wKQj7ZumfXKTgghb?dl=0
You don't have to use all the pictures; just a few.

Friendwall page:
https://www.friendwall.example/Grins-of-Maplecrest-527163048915276

Colors: Calming colors/images for a soothing feeling... to assure the patient that it'll not be that bad.

Target Market(s)

General population

Industry/Entity Type

Dental Clinic

Coding

Coded - Design and coding required

Number of Pages Required

5+ page

Requirements
Must have
• About us, contact us, services, our offices, our staff, patient education, patient forms (link to Molvaro can be used here), link to friendwall, testimonials.
• Just create the placeholders for content or use from existing website.
• The staff picture of everyone needs to be on the home page - because that makes it more personal and has received positive feedback from many patients.

```html
<!DOCTYPE html>
<html lang="en">
<head>
<meta charset="utf-8">
<title>Grins of Maplecrest - Dental</title>
<link rel="stylesheet" href="https://fonts.googleapis.com/css2?family=Open+Sans:ital,wght@0,400;0,600;0,700;1,400&display=swap">
<style>
:root{
  --teal:#2db4bd;
  --teal-dark:#25a3ad;
  --purple:#8c6fe0;
  --sky:#d8f2fa;
  --ink:#333a40;
  --muted:#666d73;
  --line:#e4e8ea;
  --white:#fff;
  --foot-bar:#e9ebec;
  --tick:#f0a72b;
}
*{box-sizing:border-box;margin:0;padding:0}
html,body{width:1200px;height:3600px;overflow:hidden}
body{font-family:"Open Sans",Arial,sans-serif;color:var(--ink);background:var(--white);position:relative}
a{color:inherit;text-decoration:none}

/* header */
.site-header{position:absolute;left:0;top:0;width:1200px;height:96px}
.brand{position:absolute;left:100px;top:24px;display:flex;align-items:center;gap:12px;font-size:28px;color:var(--ink)}
.brand-dot{width:34px;height:34px;border-radius:50%;background:var(--purple);flex:none}
.follow{position:absolute;left:672px;top:34px;display:flex;align-items:center;gap:8px;font-size:14px;color:var(--muted)}
.social{width:28px;height:28px;border-radius:50%;background:var(--teal)}
.social.alt{background:var(--teal-dark)}
.btn-appt{position:absolute;left:912px;top:27px;width:190px;height:42px;border-radius:21px;background:var(--purple);color:var(--white);font-size:14px;font-weight:600;display:flex;align-items:center;justify-content:center}

.main-nav{position:absolute;left:0;top:96px;width:1200px;height:48px;background:var(--teal);border-top:3px solid var(--teal-dark)}
.main-nav ul{list-style:none;display:flex;height:100%;padding-left:100px}
.main-nav li{font-size:11.5px;color:var(--white);font-weight:600;padding:0 22px;display:flex;align-items:center}
.main-nav li.active{background:var(--purple)}

/* hero */
.hero-photo{position:absolute;left:0;top:144px;width:1200px;height:456px;background:linear-gradient(180deg,#a89078 0%,#7d6858 40%,#2f2a2a 75%,#1f1c1d 100%)}
.hero-caption{position:absolute;left:100px;top:408px;width:516px;height:137px;background:rgba(140,111,224,.94);color:var(--white);padding:18px 36px}
.hero-caption h1{font-size:28px;font-weight:700;line-height:1.2}
.hero-caption .sub{font-size:17px;margin-top:4px}
.hero-caption .tag{font-size:26px;margin-top:0;white-space:nowrap}

/* welcome */
.section-title{font-size:29px;font-weight:600;color:var(--teal-dark);text-align:center}
.welcome-title{position:absolute;top:656px;left:0;width:1200px}
.welcome-text{position:absolute;top:712px;left:160px;width:880px;text-align:center;font-size:13px;line-height:26px;color:var(--muted)}
.service{position:absolute;top:816px;width:240px;text-align:center}
.service svg{display:block;margin:0 auto}
.service h3{font-size:14.5px;font-weight:600;margin-top:26px;color:var(--ink)}
.service p{font-size:11px;line-height:19px;color:var(--muted);margin:12px auto 0;width:200px}

/* offices */
.offices{position:absolute;top:1164px;left:0;width:1200px;height:396px}
.offices-photo{position:absolute;left:0;top:0;width:600px;height:396px;background:linear-gradient(180deg,#d6e6ee 0%,#9c6a55 38%,#8a5a48 58%,#7aa05a 80%,#5e8440 100%)}
.offices-panel{position:absolute;left:600px;top:0;width:600px;height:396px;background:var(--purple);color:var(--white);padding:58px 110px 0 110px}
.offices-panel h2{font-size:29px;font-weight:600}
.offices-panel p{font-size:11.5px;line-height:21px;margin-top:16px}
.btn-ghost{display:inline-flex;align-items:center;justify-content:center;width:154px;height:44px;border:1.5px solid var(--white);border-radius:22px;font-size:12px;margin-top:28px}

/* team */
.team{position:absolute;top:1560px;left:0;width:1200px;height:852px;background:var(--sky)}
.team .section-title{position:absolute;top:62px;width:1200px}
.team-intro{position:absolute;top:118px;left:230px;width:740px;text-align:center;font-size:13.5px;line-height:26px;color:var(--ink)}
.member{position:absolute;width:480px;height:216px}
.member-photo{position:absolute;left:0;top:0;width:221px;height:216px}
.tone-a{background:linear-gradient(180deg,#a06f52 0%,#6b4a3c 55%,#24201f 100%)}
.tone-b{background:linear-gradient(180deg,#b7896b 0%,#85604c 55%,#2a2423 100%)}
.tone-c{background:linear-gradient(180deg,#8c7a6c 0%,#6a5548 55%,#262222 100%)}
.tone-d{background:linear-gradient(180deg,#b9a493 0%,#c9a27a 50%,#2b2626 100%)}
.member-bar{position:absolute;left:0;bottom:0;width:221px;height:40px;background:var(--purple);color:var(--white);font-size:12px;font-weight:600;display:flex;align-items:center;justify-content:center}
.member-info{position:absolute;left:264px;top:4px;width:200px}
.member-info h4{font-size:16px;font-weight:600;color:var(--teal-dark)}
.member-info .role{font-size:15px;margin-top:8px}
.member-info p{font-size:11px;line-height:19px;color:var(--muted);margin-top:10px}
.btn-book{position:absolute;left:264px;top:168px;width:174px;height:36px;border-radius:18px;background:var(--teal);color:var(--white);font-size:12px;font-weight:600;display:flex;align-items:center;justify-content:center}
.btn-more{position:absolute;left:482px;top:744px;width:236px;height:48px;border-radius:24px;background:var(--purple);color:var(--white);font-size:13px;font-weight:600;display:flex;align-items:center;justify-content:center}

/* patient form */
.patient-photo{position:absolute;left:100px;top:2484px;width:520px;height:380px;background:linear-gradient(135deg,#ece6df 0%,#d4c4b4 40%,#b89a86 65%,#e58a4e 100%);border:4px solid var(--line)}
.patient-copy{position:absolute;left:684px;top:2484px;width:420px}
.patient-copy h2{font-size:29px;font-weight:600;color:var(--teal-dark)}
.patient-copy .lead{font-size:13.5px;line-height:26px;margin-top:8px}
.patient-copy .lead a{color:var(--purple);font-weight:600;font-size:15px}
.ticks{list-style:none;margin-top:10px}
.ticks li{display:flex;align-items:center;gap:12px;font-size:13px;height:30px;border-bottom:1px solid var(--line)}
.ticks li:last-child{border-bottom:0}

/* testimonial */
.testimonial{position:absolute;top:2934px;left:0;width:1200px;height:350px;background:var(--teal);color:var(--white);text-align:center}
.quote-mark{position:absolute;left:560px;top:52px}
.testimonial blockquote{position:absolute;left:180px;top:112px;width:840px;font-size:13px;font-style:italic;line-height:28px}
.avatar{position:absolute;left:476px;top:196px;width:64px;height:64px;border-radius:50%;background:linear-gradient(180deg,#b88a6c,#5a3f33);border:3px solid var(--white)}
.cite{position:absolute;left:562px;top:210px;text-align:left}
.cite strong{font-size:14px;display:block}
.cite span{font-size:11px}
.dots{position:absolute;left:570px;top:304px;display:flex;gap:6px}
.dots i{width:6px;height:6px;border-radius:50%;background:rgba(255,255,255,.5)}
.dots i.on{background:var(--white)}

/* footer */
.site-footer{position:absolute;top:3284px;left:0;width:1200px;height:268px}
.footer-brand{position:absolute;left:110px;top:40px;width:160px;display:flex;flex-direction:column;align-items:center;gap:8px;font-size:22px;line-height:26px;color:var(--ink);text-align:center}
.footer-brand .brand-dot{width:56px;height:56px}
.fcol{position:absolute;top:40px}
.fcol h5{font-size:15px;font-weight:700;color:var(--teal-dark);margin-bottom:14px}
.fcol p,.fcol li{font-size:11.5px;line-height:22px;color:var(--ink);list-style:none}
.contact-line{display:flex;align-items:center;gap:10px}
.hours{border-collapse:collapse}
.hours td{font-size:11.5px;line-height:22px;vertical-align:top;padding:0}
.hours td:first-child{width:150px}
.copyright{position:absolute;top:3552px;left:0;width:1200px;height:48px;background:var(--foot-bar);font-size:11px;color:var(--muted);display:flex;align-items:center;justify-content:center}
</style>
</head>
<body>

<header class="site-header">
  <div class="brand"><span class="brand-dot"></span>Grins of Maplecrest</div>
  <div class="follow">Follow Us :
    <span class="social"></span><span class="social alt"></span><span class="social"></span><span class="social alt"></span>
  </div>
  <a class="btn-appt" href="#">Make an appointment</a>
</header>

<nav class="main-nav">
  <ul>
    <li class="active">HOME</li><li>ABOUT US</li><li>SERVICES</li><li>OUR OFFICES</li><li>OUR STAFF</li><li>PATIENT EDUCATION</li><li>PATIENT FORMS</li><li>TESTIMONIALS</li><li>CONTACT US</li>
  </ul>
</nav>

<div class="hero-photo" role="img" aria-label="Group photo of the five members of the dental team in front of a stone fireplace"></div>
<div class="hero-caption">
  <h1>Dr. Priya Natarajan, DDS</h1>
  <div class="sub">Grins of Maplecrest</div>
  <div class="tag">Honestly Caring &amp; Quality Dentistry</div>
</div>

<h2 class="section-title welcome-title">A Warm Welcome to You &amp; Your Family</h2>
<p class="welcome-text">Dr. Natarajan graduated from the Pacific Crest University and has been practicing dentistry for more than twenty years.<br>She moved from Cedar Bluff, TX to this area and is enjoying the small town feel very much.</p>

<div class="service" style="left:84px">
  <svg width="118" height="144" viewBox="0 0 118 144"><path d="M59 0 C59 0 118 62 118 85 A59 59 0 0 1 0 85 C0 62 59 0 59 0Z" fill="var(--purple)"/><path d="M40 62c8-6 14-2 19 0 5-2 11-6 19 0 7 6 4 20 0 30-3 8-3 22-8 22-5 0-4-16-11-16s-6 16-11 16c-5 0-5-14-8-22-4-10-7-24 0-30Z" fill="none" stroke="var(--white)" stroke-width="4"/></svg>
  <h3>General Dental Health</h3>
  <p>Fillings are done to remove decay, and replace the affected tooth structure. It is called a filling because new a material...</p>
</div>
<div class="service" style="left:348px">
  <svg width="118" height="144" viewBox="0 0 118 144"><path d="M59 0 C59 0 118 62 118 85 A59 59 0 0 1 0 85 C0 62 59 0 59 0Z" fill="var(--teal)"/><path d="M26 76 Q59 70 92 76 Q86 112 59 112 Q32 112 26 76Z" fill="var(--white)"/><path d="M34 84 H84 M46 78 V104 M59 76 V110 M72 78 V104" stroke="var(--teal)" stroke-width="2.5"/></svg>
  <h3>Cosmetic Dentistry</h3>
  <p>Fillings are done to remove decay, and replace the affected tooth structure. It is called a filling because new a material...</p>
</div>
<div class="service" style="left:612px">
  <svg width="118" height="144" viewBox="0 0 118 144"><path d="M59 0 C59 0 118 62 118 85 A59 59 0 0 1 0 85 C0 62 59 0 59 0Z" fill="var(--teal)"/><path d="M40 62c8-6 14-2 19 0 5-2 11-6 19 0 7 6 4 20 0 30-3 8-3 22-8 22-5 0-4-16-11-16s-6 16-11 16c-5 0-5-14-8-22-4-10-7-24 0-30Z" fill="var(--white)"/><path d="M52 72 L70 90" stroke="var(--teal)" stroke-width="4"/></svg>
  <h3>Dental FAQs</h3>
  <p>Fillings are done to remove decay, and replace the affected tooth structure. It is called a filling because new a material...</p>
</div>
<div class="service" style="left:876px">
  <svg width="118" height="144" viewBox="0 0 118 144"><path d="M59 0 C59 0 118 62 118 85 A59 59 0 0 1 0 85 C0 62 59 0 59 0Z" fill="var(--teal)"/><path d="M30 100 H88 M40 100 V84 H80 V100 M50 84 L44 60 M70 84 L86 66" stroke="var(--white)" stroke-width="5" fill="none" stroke-linecap="round"/></svg>
  <h3>Advanced Dental Procedures</h3>
  <p>Fillings are done to remove decay, and replace the affected tooth structure. It is called a filling because new a material...</p>
</div>

<section class="offices">
  <div class="offices-photo" role="img" aria-label="Photo of the brick dental office building with a green lawn and trees"></div>
  <div class="offices-panel">
    <h2>Our Offices</h2>
    <p>Please tour our web site to learn more about family dentistry, cosmetic dentistry and our restorative dental services. We invite you to call us with any questions you may have - we all look forward to meeting you and your family!</p>
    <p>New patients looking for quality dental care in a relaxed environment are welcome! We accept PPO, Indemnity and Traditional insurance plans.</p>
    <a class="btn-ghost" href="#">Read more info</a>
  </div>
</section>

<section class="team">
  <h2 class="section-title">Meet our team</h2>
  <p class="team-intro">Lorem Ipsum is simply dummy text of the printing and typesetting industry. Lorem Ipsum has been the industry's standard dummy text ever since the 1500</p>

  <div class="member" style="left:96px;top:211px">
    <div class="member-photo tone-a" role="img" aria-label="Portrait of Dr. Priya Natarajan"></div>
    <div class="member-bar">Click here for view details</div>
    <div class="member-info"><h4>Dr. Priya Natarajan</h4><div class="role">Specialist dentistry</div><p>Dr. Natarajan graduated from the Pacific Crest University and has been practicing dentistry for more than twenty years...</p></div>
    <a class="btn-book" href="#">Book Appointment</a>
  </div>
  <div class="member" style="left:629px;top:211px">
    <div class="member-photo tone-b" role="img" aria-label="Portrait of Kelsey Marlow"></div>
    <div class="member-bar">Click here for view details</div>
    <div class="member-info"><h4>Kelsey Marlow</h4><div class="role">Specialist dentistry</div><p>Kelsey is our multi-talented office manager who not only runs the front office, but also helps patients in any way possible...</p></div>
    <a class="btn-book" href="#">Book Appointment</a>
  </div>
  <div class="member" style="left:96px;top:475px">
    <div class="member-photo tone-c" role="img" aria-label="Portrait of Lena Corvell"></div>
    <div class="member-bar">Click here for view details</div>
    <div class="member-info"><h4>Lena Corvell</h4><div class="role">Specialist dentistry</div><p>Lena joined our practice as a dental hygienist and has been caring for patients of every age for many years...</p></div>
    <a class="btn-book" href="#">Book Appointment</a>
  </div>
  <div class="member" style="left:629px;top:475px">
    <div class="member-photo tone-d" role="img" aria-label="Portrait of Jenna Albright"></div>
    <div class="member-bar">Click here for view details</div>
    <div class="member-info"><h4>Jenna Albright</h4><div class="role">Specialist dentistry</div><p>Jenna is our friendly dental assistant who not only helps in the chair, but also helps patients in any way possible...</p></div>
    <a class="btn-book" href="#">Book Appointment</a>
  </div>

  <a class="btn-more" href="#">View more staffs details</a>
</section>

<div class="patient-photo" role="img" aria-label="Photo of the dentist talking with a patient in the treatment chair"></div>
<div class="patient-copy">
  <h2>New Patient Form</h2>
  <p class="lead">If you are a new patient, you may find it convenient to fill out the <a href="#">New Patient Forms online</a> before you visit us.</p>
  <ul class="ticks">
    <li><svg width="12" height="10" viewBox="0 0 12 10"><path d="M1 5 L4.5 8.5 L11 1" stroke="var(--tick)" stroke-width="2" fill="none"/></svg>Saturday &amp; Tuesday late appointments</li>
    <li><svg width="12" height="10" viewBox="0 0 12 10"><path d="M1 5 L4.5 8.5 L11 1" stroke="var(--tick)" stroke-width="2" fill="none"/></svg>Kid friendly environment</li>
    <li><svg width="12" height="10" viewBox="0 0 12 10"><path d="M1 5 L4.5 8.5 L11 1" stroke="var(--tick)" stroke-width="2" fill="none"/></svg>State of the art digital X-ray</li>
    <li><svg width="12" height="10" viewBox="0 0 12 10"><path d="M1 5 L4.5 8.5 L11 1" stroke="var(--tick)" stroke-width="2" fill="none"/></svg>Emergencies welcome</li>
    <li><svg width="12" height="10" viewBox="0 0 12 10"><path d="M1 5 L4.5 8.5 L11 1" stroke="var(--tick)" stroke-width="2" fill="none"/></svg>Preventive, restorative &amp; cosmetic dentistry</li>
    <li><svg width="12" height="10" viewBox="0 0 12 10"><path d="M1 5 L4.5 8.5 L11 1" stroke="var(--tick)" stroke-width="2" fill="none"/></svg>Root canal treatment</li>
    <li><svg width="12" height="10" viewBox="0 0 12 10"><path d="M1 5 L4.5 8.5 L11 1" stroke="var(--tick)" stroke-width="2" fill="none"/></svg>Extractions</li>
    <li><svg width="12" height="10" viewBox="0 0 12 10"><path d="M1 5 L4.5 8.5 L11 1" stroke="var(--tick)" stroke-width="2" fill="none"/></svg>Dentures</li>
    <li><svg width="12" height="10" viewBox="0 0 12 10"><path d="M1 5 L4.5 8.5 L11 1" stroke="var(--tick)" stroke-width="2" fill="none"/></svg>Periodontal treatment</li>
    <li><svg width="12" height="10" viewBox="0 0 12 10"><path d="M1 5 L4.5 8.5 L11 1" stroke="var(--tick)" stroke-width="2" fill="none"/></svg>and much more.......</li>
  </ul>
</div>

<section class="testimonial">
  <svg class="quote-mark" width="80" height="40" viewBox="0 0 80 40"><path d="M22 8 Q12 12 12 24 V34 H28 V20 H20 Q20 14 26 12Z M50 8 Q40 12 40 24 V34 H56 V20 H48 Q48 14 54 12Z" fill="var(--white)"/></svg>
  <blockquote>Lorem Ipsum is simply dummy text of the printing and typesetting industry. Lorem Ipsum has been the industry's standard dummy text ever since the 1500s, when an unknown printer took a galley of type and scrambled it to make a type specimen book</blockquote>
  <div class="avatar" role="img" aria-label="Small portrait of the reviewer"></div>
  <div class="cite"><strong>LENA CORVELL</strong><span>House wife</span></div>
  <div class="dots"><i class="on"></i><i></i><i></i></div>
</section>

<footer class="site-footer">
  <div class="footer-brand"><span class="brand-dot"></span>Grins of<br>Maplecrest</div>
  <div class="fcol" style="left:336px">
    <h5>Grins of Maplecrest</h5>
    <p>418 Larkspur Ave, Suite 2C</p>
    <p>Maplecrest, IL 60000</p>
    <p class="contact-line"><svg width="12" height="12" viewBox="0 0 12 12"><path d="M2 1 L4 1 L5 4 L3.5 5 Q5 7.5 7 8.5 L8 7 L11 8 L11 10 Q10 11 8 11 Q1 8 1 2Z" fill="var(--purple)"/></svg>555-014-2210/2212</p>
    <p class="contact-line"><svg width="12" height="12" viewBox="0 0 12 12"><rect x="0.5" y="2" width="11" height="8" fill="var(--purple)"/><path d="M1 2.5 L6 6.5 L11 2.5" stroke="var(--white)" fill="none"/></svg>info@grinsofmaplecrest.example</p>
    <p class="contact-line"><svg width="12" height="12" viewBox="0 0 12 12"><circle cx="6" cy="6" r="5.5" fill="var(--purple)"/></svg>www.grinsofmaplecrest.example</p>
  </div>
  <div class="fcol" style="left:648px">
    <h5>Welcome</h5>
    <ul><li>About us</li><li>Services</li><li>our offices</li><li>Our staff</li><li>Patient education</li><li>Patient forms</li><li>Testimonials</li></ul>
  </div>
  <div class="fcol" style="left:821px">
    <h5>Opening Hours</h5>
    <table class="hours">
      <tr><td>Monday</td><td>: 12:00pm to 6:00pm</td></tr>
      <tr><td>Tuesday</td><td>: 10:00am to 7:00pm</td></tr>
      <tr><td>Wednesday</td><td>: Closed</td></tr>
      <tr><td>Thursday</td><td>: 8:00am to 6:00pm</td></tr>
      <tr><td>Friday</td><td>: 8:00am to 5:00pm</td></tr>
      <tr><td>Saturday when open</td><td>: 8:00am to 3:00pm OR<br>&nbsp;&nbsp;8:00am to 12:00pm</td></tr>
    </table>
  </div>
</footer>
<div class="copyright">Copyright © Grins of Maplecrest. 2016.All rights reserved.</div>

</body>
</html>
```